Waste Oil Filter collection & disposal

Basically I need a 1 page website for the business called Brenmoor Waste Solutions.
We are a environmental service provider and we collect and dispose of waste oil filters to protect the environment from hazardous waste oil products.

This is the link to our current website: www.brenmoorwaste.co.nz

we want it to look fresh and better than our current website. we may potentially look at getting a new logo designed and are open to ideas/designs if you have any.

Industry/Entity Type

Business

Logo Text

Brenmoor Waste Solutions

Number of Pages Required

1 page

Requirements
Must have
• same colours as current website.
• description of what service we provide please refer to leaflet attached

```html
<!DOCTYPE html>
<html lang="en">
<head>
<meta charset="utf-8">
<title>Brenmoor Waste Solutions</title>
<link rel="stylesheet" href="https://fonts.googleapis.com/css2?family=Lato:ital,wght@0,300;0,400;0,700;1,400&display=swap">
<style>
:root{
  --green:#00855f;
  --nav:#2f5d10;
  --ink:#1e1e1e;
  --muted:#5a5a5a;
  --grey:#c1c0bc;
  --footer:#5f5f5f;
  --white:#ffffff;
  --tile:#c4c4c4;
}
*{box-sizing:border-box;margin:0;padding:0}
html,body{width:1200px;height:3750px;overflow:hidden}
body{font-family:'Lato',sans-serif;color:var(--ink);background:var(--white);position:relative}
.abs{position:absolute}

/* header */
.site-header{left:0;top:0;width:1200px;height:143px;background:var(--white)}
.brand{left:22px;top:52px;display:flex;align-items:center;gap:14px}
.brand-dot{width:34px;height:34px;border-radius:50%;background:var(--green)}
.brand-name{font-weight:700;font-size:26px;color:var(--nav)}
.main-nav{right:68px;top:92px;display:flex;gap:0}
.main-nav a{font-size:19px;color:var(--nav);text-decoration:none;margin-left:44px}

/* hero */
.hero{left:0;top:143px;width:1200px;height:465px;background:linear-gradient(180deg,#8fb4d6 0%,#c9d8e4 30%,#5f6b6e 48%,#5f9a3a 62%,#6b5fb8 82%,#4a3f8a 100%)}
.hero-band{left:0;top:345px;width:1200px;height:105px;background:rgba(40,70,40,.55)}
.hero-title{left:0;top:360px;width:1200px;text-align:center;font-style:italic;font-size:52px;color:var(--white)}
.hero-arrow{top:372px}

/* intro */
.intro{left:118px;top:638px;width:960px;font-size:21.5px;line-height:27px;color:var(--muted)}
.intro p{margin-bottom:27px}
.intro strong{font-size:27px;color:var(--ink)}
.prices{left:118px;top:913px;width:955px;font-size:28px;font-weight:700;display:flex;justify-content:space-between;white-space:nowrap}
.prices span{flex:none}
.quick{top:975px;width:200px;text-align:center}
.quick .ring{width:110px;height:110px;border-radius:50%;background:var(--green);margin:0 auto;display:flex;align-items:center;justify-content:center}
.quick span{display:block;font-size:32px;color:var(--green);margin-top:14px}

/* process */
.process{left:0;top:1153px;width:1200px;height:535px;background:var(--green);color:var(--white)}
.section-title{font-weight:300;font-size:46px;letter-spacing:1px}
.process .section-title{position:absolute;left:118px;top:38px}
.process .lead{position:absolute;left:118px;top:92px;font-size:20px;color:rgba(255,255,255,.8)}
.step{top:175px;width:130px;text-align:center}
.step b{display:block;font-size:13px;line-height:16px;height:40px}
.process .oil-title{position:absolute;left:118px;top:380px}
.process .oil-text{position:absolute;left:118px;top:432px;width:960px;font-size:20px;line-height:26px;color:rgba(255,255,255,.85)}

/* journal */
.journal-title{left:118px;top:1710px;color:var(--ink)}
.entry{left:118px;width:900px;display:flex;gap:25px}
.entry-thumb{width:112px;height:110px;background:var(--tile);flex:none}
.entry q{display:block;font-weight:700;font-size:32px;line-height:40px;quotes:'"' '"'}
.entry small{display:block;font-size:15px;color:var(--muted);margin-top:12px}

/* gallery */
.gallery{left:0;top:2288px;width:1200px;height:707px;background:var(--grey)}
.gallery-head{position:absolute;left:118px;top:32px;display:flex;align-items:baseline;gap:20px}
.gallery-head span{font-size:20px;color:#333}
.tile{position:absolute;width:267px;height:243px}
.tile .photo{width:100%;height:200px}
.tile .cap{height:43px;background:var(--green);color:var(--white);font-size:16px;padding:13px 14px}

/* contact */
.contact{left:0;top:2995px;width:1200px;height:638px;background:var(--green);color:var(--white)}
.contact .section-title{position:absolute;left:118px;top:38px}
.field-label{position:absolute;left:93px;font-size:20px;color:#d9efe6}
.field{position:absolute;left:213px;width:567px;height:55px;background:var(--white)}
.info{position:absolute;left:823px;top:135px;width:360px;color:#d9efe6}
.info h3{font-weight:400;font-size:27px;color:#e7f5ef;white-space:nowrap}
.info p{font-size:16px;line-height:20px;margin-top:6px}
.submit{position:absolute;left:820px;top:510px;width:105px;height:25px;border:2px solid #0b3b2a;color:#0b3b2a;font-size:10px;text-align:center;line-height:21px;letter-spacing:1px}

/* footer */
.site-footer{left:0;top:3633px;width:1200px;height:117px;background:var(--footer);color:var(--white)}
.site-footer p{position:absolute;left:88px;top:46px;font-size:16px;font-weight:700}
.social{position:absolute;left:822px;top:40px;display:flex;gap:14px}
.social i{width:26px;height:26px;border-radius:50%;background:var(--white);display:block}
</style>
</head>
<body>

<header class="site-header abs">
  <div class="brand abs"><div class="brand-dot"></div><div class="brand-name">Brenmoor Waste Solutions</div></div>
  <nav class="main-nav abs"><a href="#">HOME</a><a href="#">ABOUT US</a><a href="#">THE PROCESS</a><a href="#">GALLERY</a><a href="#">CONTACT US</a></nav>
</header>

<section class="hero abs" role="img" aria-label="Landscape of mountains above a lake with a field of purple lupins"></section>
<div class="hero-band abs"></div>
<svg class="hero-arrow abs" style="left:8px" width="30" height="50" viewBox="0 0 30 50"><path d="M24 4 6 25l18 21" fill="none" stroke="#fff" stroke-width="4"/></svg>
<svg class="hero-arrow abs" style="right:8px" width="30" height="50" viewBox="0 0 30 50"><path d="M6 4l18 21L6 46" fill="none" stroke="#fff" stroke-width="4"/></svg>
<h1 class="hero-title abs">Keeping New Zealand Green</h1>

<section class="intro abs">
  <p><strong>Brenmoor Waste Solutions</strong> specialize in the collection &amp; disposal of oil / fuel filters, servicing the lower north island on a monthly cycle. We offer a cost effective environmentally friendly system for the collection and disposal of waste oil filters helping minimise contamination of landfills keeping your industry compliant.</p>
  <p>Brenmoor Waste Solutions service the Lower North Island and specialise in the collection &amp; disposal of oil &amp; fuel filters.</p>
  <p>Talk to us on how we can you help keep New Zealand green.</p>
</section>
<div class="prices abs"><span>Monthly Bin Collection: $65</span><span>Additional Bins: $35 ea</span><span>Account Set up&nbsp; $85</span></div>

<div class="quick abs" style="left:275px"><div class="ring">
  <svg width="64" height="64" viewBox="0 0 64 64" fill="none" stroke="#fff" stroke-width="5"><path d="M32 8 18 30M46 30 32 8M10 44h28M54 44h-8"/><path d="M12 26l6 4 4-7M52 26l-6 4-4-7M44 50l-6-6 6-6"/></svg>
</div><span>The Process</span></div>
<div class="quick abs" style="left:500px"><div class="ring">
  <svg width="64" height="64" viewBox="0 0 64 64" fill="#fff"><path d="M10 22c0-6 44-6 44 0v6h-10v-5H20v5H10z"/><path d="M16 32h32l4 20H12z"/><circle cx="32" cy="42" r="6" fill="#00855f"/></svg>
</div><span>Contact Us</span></div>
<div class="quick abs" style="left:725px"><div class="ring">
  <svg width="64" height="64" viewBox="0 0 64 64" fill="none" stroke="#fff" stroke-width="4"><rect x="14" y="16" width="38" height="30" transform="rotate(-8 33 31)"/><rect x="10" y="22" width="38" height="30"/><path d="M14 48l10-12 8 8 6-6 8 10"/><circle cx="38" cy="31" r="3"/></svg>
</div><span>Gallery</span></div>

<section class="process abs">
  <h2 class="section-title">THE PROCESS</h2>
  <p class="lead">Filters are collected and transported back to the processing plant. At the processing plant they are:</p>

  <div class="step abs" style="left:188px"><b><br>DRAINED</b>
    <svg width="60" height="80" viewBox="0 0 60 80"><path d="M30 4C22 24 10 36 10 52a20 20 0 0 0 40 0C50 36 38 24 30 4z" fill="#fff"/><text x="30" y="64" text-anchor="middle" font-family="Lato,sans-serif" font-size="22" font-weight="700" fill="#00855f">1</text></svg></div>
  <div class="step abs" style="left:310px"><b><br>SORTED</b>
    <svg width="60" height="80" viewBox="0 0 60 80" fill="#fff"><rect x="14" y="14" width="10" height="56"/><rect x="14" y="14" width="34" height="10"/><rect x="14" y="37" width="34" height="10"/><rect x="14" y="60" width="34" height="10"/></svg></div>
  <div class="step abs" style="left:430px"><b>DRAINED<br>AGAIN</b>
    <svg width="60" height="80" viewBox="0 0 60 80"><path d="M30 4C22 24 10 36 10 52a20 20 0 0 0 40 0C50 36 38 24 30 4z" fill="#fff"/><text x="30" y="64" text-anchor="middle" font-family="Lato,sans-serif" font-size="22" font-weight="700" fill="#00855f">2</text></svg></div>
  <div class="step abs" style="left:570px"><b>CRUSHED<br>INTO BRICKS</b>
    <svg width="90" height="80" viewBox="0 0 90 80" fill="#fff"><path d="M6 38l44-14 34 10-44 16z"/><path d="M6 42l34 12v14L6 56zM44 54l40-16v14L44 68z"/></svg></div>
  <div class="step abs" style="left:698px"><b>DRAINED FOR<br>THE 3RD TIME</b>
    <svg width="60" height="80" viewBox="0 0 60 80"><path d="M30 4C22 24 10 36 10 52a20 20 0 0 0 40 0C50 36 38 24 30 4z" fill="#fff"/><text x="30" y="64" text-anchor="middle" font-family="Lato,sans-serif" font-size="22" font-weight="700" fill="#00855f">3</text></svg></div>
  <div class="step abs" style="left:875px"><b>STACKED FOR<br>METAL RECYCLING</b>
    <svg width="120" height="100" viewBox="0 0 120 100" fill="#fff" stroke="#00855f" stroke-width="3"><path d="M12 30l48-20 48 20-48 20z"/><path d="M12 30v48l48 20V50z"/><path d="M108 30v48L60 98V50z"/><path d="M12 54l48 20 48-20M36 40v48M84 40v48" fill="none"/></svg></div>

  <h2 class="section-title oil-title">WHAT HAPPENS TO THE OIL?</h2>
  <p class="oil-text">All residual oil is collected into our tank and then recycled.&nbsp; Currently we are processing over 2,000 litres of oil a month.</p>
</section>

<h2 class="section-title journal-title abs">JOURNAL</h2>
<article class="entry abs" style="top:1788px"><div class="entry-thumb" role="img" aria-label="Journal image"></div><div><q>each used oil filter has on average, more than quarter of a litre of used motor oil </q><small>- EcoCycle Agency</small></div></article>
<article class="entry abs" style="top:1951px"><div class="entry-thumb" role="img" aria-label="Journal image"></div><div><q>recycling engine oil protects the environment and conserves energy resources </q><small>- Oil Recycling</small></div></article>
<article class="entry abs" style="top:2111px"><div class="entry-thumb" role="img" aria-label="Journal image"></div><div><q>one litre of used oil can contaminate one million litres of water </q><small>- Harbour City Council</small></div></article>

<section class="gallery abs">
  <div class="gallery-head"><h2 class="section-title">GALLERY</h2><span>Click on picture to details.</span></div>
  <figure class="tile" style="left:123px;top:105px"><div class="photo" role="img" aria-label="Green and white collection truck" style="background:linear-gradient(160deg,#9aa59c,#3f7a52 60%,#6d6d6d)"></div><figcaption class="cap">Purpose built vehicles</figcaption></figure>
  <figure class="tile" style="left:468px;top:105px"><div class="photo" role="img" aria-label="Green filter press machine in a workshop" style="background:linear-gradient(160deg,#c9cfcc,#1f8a6b 55%,#5b6460)"></div><figcaption class="cap">Filter Press</figcaption></figure>
  <figure class="tile" style="left:808px;top:105px"><div class="photo" role="img" aria-label="Filter processing machine with stacked filters" style="background:linear-gradient(160deg,#d8d8d8,#4f5a58 55%,#2d3434)"></div><figcaption class="cap">Filter Processing Machine</figcaption></figure>
  <figure class="tile" style="left:123px;top:390px"><div class="photo" role="img" aria-label="Filter bailer machine in a workshop" style="background:linear-gradient(160deg,#b9c4c2,#2f7f77 50%,#4d4d4d)"></div><figcaption class="cap">Filter Bailer</figcaption></figure>
  <figure class="tile" style="left:468px;top:390px"><div class="photo" role="img" aria-label="Crushed brick of used oil filters" style="background:linear-gradient(160deg,#5a6670,#2a2e36 50%,#7a3b35)"></div><figcaption class="cap">Brick of Filters</figcaption></figure>
  <figure class="tile" style="left:808px;top:390px"><div class="photo" role="img" aria-label="Pallet of crushed filter bricks" style="background:linear-gradient(160deg,#6f6f7a,#3d3f55 50%,#8a6e62)"></div><figcaption class="cap">Pallet of bricks</figcaption></figure>
</section>

<section class="contact abs">
  <h2 class="section-title">CONTACT US</h2>
  <span class="field-label" style="top:165px">Name *</span><div class="field" style="top:150px"></div>
  <span class="field-label" style="top:233px">Email*</span><div class="field" style="top:223px"></div>
  <span class="field-label" style="top:305px">Subject</span><div class="field" style="top:295px"></div>
  <span class="field-label" style="top:375px">Message *</span><div class="field" style="top:363px;height:172px"></div>
  <div class="info">
    <h3>Contact Information</h3>
    <p>We collect used filters across the lower<br>North Island every month.</p>
    <h3 style="margin-top:34px">Brenmoor Waste Solutions</h3>
    <p>Harlow Road, Kaitara 4820, New Zealand</p>
    <p style="margin-top:22px">email: info@brenmoorwaste.co.nz<br>Phone: 06 555 0142</p>
  </div>
  <div class="submit">SUBMIT</div>
</section>

<footer class="site-footer abs">
  <p>Copyright © 2018&nbsp; Brenmoor Waste Solutions LTD. All Rights Reserved.</p>
  <div class="social"><i></i><i></i><i></i><i></i></div>
</footer>

</body>
</html>
```